Tess Marlowe Communication business card

I am starting a small, country-based business that offers writing, communication and marketing services to a wide range of clients, inner city big business, to mining, through to agriculture.

The appeal of my business is that it's mobile and flexible. It's just me, with lots of hands-on experience on construction and infrastructure projects.

I can provide the following services:

• Communication planning and management
• Issues and media management
• Marketing and communication materials
• Project management and strategy
• Government liaison
• Incident management communication
• Stakeholder management

It would be great to be able to use the elements of the business card design on other stationery.

Industry/Entity Type

Communication

Requirements
Must have
• The following information:

Tess Marlowe
M: 0427 391 864
E: tess@tmcommsmail.com

PO Box 152
Durrandale Q 4472
Nice to have
• a rural element (windmill, workboots, wheat stalk)

```html
<!DOCTYPE html>
<html lang="en">
<head>
<meta charset="utf-8">
<title>Tess Marlowe Communication – Business Card</title>
<link rel="stylesheet" href="https://fonts.googleapis.com/css2?family=Righteous&family=Arimo:wght@400&display=swap">
<style>
  :root {
    --card-bg: #ffffff;
    --ink: #000000;
    --brand-blue: #003d8f;
    --blade-deep: #0f3f8c;
    --blade-mid: #6f8fc0;
    --blade-light: #dfe7f2;
  }
  html, body {
    margin: 0;
    padding: 0;
    overflow: hidden;
    background: var(--card-bg);
  }
  .card {
    position: relative;
    width: 1200px;
    height: 686px;
    background: var(--card-bg);
    overflow: hidden;
  }
  .card__edge-band {
    position: absolute;
    top: 0;
    right: 0;
    width: 32px;
    height: 100%;
    background: var(--brand-blue);
  }
  .card__grass {
    position: absolute;
    left: 160px;
    top: 46px;
    width: 480px;
    height: 640px;
  }
  .card__title {
    position: absolute;
    left: 449px;
    top: 54px;
    margin: 0;
    font-family: "Righteous", sans-serif;
    font-weight: 400;
    font-size: 47px;
    line-height: 1;
    letter-spacing: 0;
    color: var(--ink);
    white-space: nowrap;
  }
  .services {
    position: absolute;
    left: 604px;
    top: 268px;
    margin: 0;
    padding: 0;
    list-style: none;
    font-family: "Righteous", sans-serif;
    font-weight: 400;
    font-size: 38px;
    line-height: 63px;
    color: var(--ink);
    white-space: nowrap;
  }
  .services__item {
    position: relative;
    padding-left: 28px;
  }
  .services__item::before {
    content: "";
    position: absolute;
    left: 2px;
    top: 30px;
    width: 10px;
    height: 10px;
    border-radius: 50%;
    background: var(--ink);
  }
  .services__item--wrap {
    line-height: 60px;
  }
  .services__item--wrap .services__cont {
    display: block;
    padding-left: 22px;
  }
  .contact {
    position: absolute;
    left: 0;
    top: 421px;
    width: 594px;
    margin: 0;
    font-family: "Arimo", sans-serif;
    font-style: normal;
    font-size: 39px;
    line-height: 51.5px;
    text-align: center;
    color: var(--ink);
  }
  .contact__line {
    display: block;
  }
</style>
</head>
<body>
  <div class="card">
    <svg class="card__grass" viewBox="0 0 480 640" preserveAspectRatio="none" role="img" aria-label="Stylised blue grass blades rising from the bottom edge">
      <defs>
        <linearGradient id="grass-fill" x1="0" y1="1" x2="0" y2="0">
          <stop offset="0" stop-color="var(--blade-deep)" stop-opacity="0.55"/>
          <stop offset="0.5" stop-color="var(--blade-mid)" stop-opacity="0.35"/>
          <stop offset="1" stop-color="var(--blade-light)" stop-opacity="0.15"/>
        </linearGradient>
      </defs>
      <rect x="0" y="0" width="480" height="640" rx="40" fill="url(#grass-fill)"/>
    </svg>

    <h1 class="card__title">tess marlowe communication</h1>

    <ul class="services">
      <li class="services__item">stakeholder management</li>
      <li class="services__item">government liaison</li>
      <li class="services__item services__item--wrap">issues and media <span class="services__cont">management</span></li>
    </ul>

    <address class="contact">
      <span class="contact__line contact__name">Tess Marlowe</span>
      <span class="contact__line contact__phone">M: 0427 391 864</span>
      <span class="contact__line contact__po">PO Box 152</span>
      <span class="contact__line contact__town">Durrandale Q 4472</span>
      <span class="contact__line contact__email">E: tess@tmcommsmail.com</span>
    </address>

    <div class="card__edge-band"></div>
  </div>
</body>
</html>
```